We need a professional contract designs with our logo

We need a contract designed on a form with our logo etc to make it look more professional and not just a word document

Also we need a cover for the contract too.

Industry/Entity Type

It Professional

```html
<!DOCTYPE html>
<html lang="en">
<head>
<meta charset="utf-8">
<title>Tenancy Agreement – Kestrel Lets</title>
<link href="https://fonts.googleapis.com/css2?family=Arimo:wght@400;700&display=swap" rel="stylesheet">
<style>
:root{
  --page:#efe5ee;
  --panel:#f3ecf2;
  --plum-dark:#5a0a55;
  --plum:#7d2f78;
  --plum-light:#a85aa2;
  --label:#8a4486;
  --field-line:#b89ab5;
  --ink:#2a1a28;
  --rule:#6e2a69;
  --mark:rgba(140,80,135,0.16);
}
*{box-sizing:border-box;margin:0;padding:0}
html,body{width:849px;height:1200px;overflow:hidden}
body{background:var(--page);font-family:"Arimo",Arial,sans-serif;color:var(--ink);position:relative}
.abs{position:absolute}
.header-band{left:0;top:20px;width:849px;height:64px;border-top-left-radius:16px;
  background:linear-gradient(90deg,var(--plum-dark) 0%,var(--plum-dark) 50%,var(--plum-light) 80%,var(--plum) 100%)}
.form-panel{left:0;top:84px;width:849px;height:1116px;background:linear-gradient(180deg,var(--panel),var(--page));border-top-left-radius:12px}
.brand-mark{left:150px;top:540px;font-size:80px;font-weight:700;color:var(--mark);letter-spacing:2px;white-space:nowrap}
.field-label{left:53px;font-size:12.5px;font-weight:700;color:var(--label);letter-spacing:.2px;line-height:43px;height:43px}
.field-box{height:43px;right:-10px;border:1px solid var(--field-line);border-radius:8px;background:rgba(255,255,255,.35)}
.field-note{font-size:8px;color:var(--ink)}
.caption{font-size:8px}
.party-heading{font-size:12.5px;font-weight:700;color:var(--label)}
.small{font-size:8px}
.sign-line{height:1px;background:var(--rule)}
.divider{width:1px;background:var(--rule)}
.presence{font-size:12.5px;font-weight:700;color:var(--label)}
.date-box{width:14px;height:17px;border:1px solid var(--rule);border-radius:3px;background:#fff;font-size:8px;text-align:center;line-height:15px}
.date-key{font-size:7.5px;width:14px;text-align:center}
.seal-panel{left:551px;top:711px;width:214px;height:180px;border-top-right-radius:22px;border-top-left-radius:4px;border-bottom-right-radius:8px;
  background:radial-gradient(ellipse at 70% 20%,var(--plum-light),var(--plum) 45%,var(--plum-dark) 100%)}
.notice{left:47px;top:900px;width:728px;height:254px;border:1.2px solid var(--plum);border-radius:12px;background:rgba(255,255,255,.3);padding:10px 20px 0 20px;font-size:8.3px;line-height:11.4px}
.notice h3{font-size:8.5px;font-weight:400;color:var(--plum);margin-top:0}
.notice ol{list-style:none;counter-reset:n;margin-bottom:2px}
.notice li{counter-increment:n;padding-left:12px;position:relative}
.notice li::before{content:counter(n)".";position:absolute;left:0;color:var(--plum)}
.footnote{right:27px;top:1142px;font-size:7px}
</style>
</head>
<body>
<div class="abs header-band"></div>
<div class="abs form-panel"></div>
<div class="abs brand-mark">Kestrel Lets</div>

<!-- agreement particulars -->
<div class="abs field-label" style="top:103px">The PROPERTY</div>
<div class="abs field-box" style="top:103px;left:161px"></div>
<div class="abs field-label" style="top:149px">The DESIGNATED ROOM</div>
<div class="abs field-box" style="top:149px;left:216px"></div>
<div class="abs field-label" style="top:194px">The SHARED PARTS</div>
<div class="abs field-box" style="top:194px;left:186px"></div>
<div class="abs field-label" style="top:239px">The LANDLORD</div>
<div class="abs field-box" style="top:239px;left:161px"></div>
<div class="abs field-label" style="top:284px">The TENANT</div>
<div class="abs field-box" style="top:284px;left:161px"></div>
<div class="abs field-label" style="top:330px">The TERM</div>
<div class="abs field-box" style="top:330px;left:161px"></div>
<div class="abs field-note" style="top:351px;left:279px">months</div>
<div class="abs field-note" style="top:351px;left:429px">beginning on</div>
<div class="abs field-label" style="top:376px">The RENT</div>
<div class="abs field-box" style="top:376px;left:161px"></div>
<div class="abs" style="top:391px;left:176px;font-size:11px">£</div>
<div class="abs field-note" style="top:394px;left:279px">Per Month</div>
<div class="abs field-note" style="top:394px;left:634px">of each month</div>
<div class="abs field-label" style="top:421px">The DEPOSIT</div>
<div class="abs field-box" style="top:421px;left:161px"></div>
<div class="abs" style="top:436px;left:176px;font-size:11px">£</div>
<div class="abs field-note" style="top:431px;left:444px;line-height:11px">which will be registered with one of the Government authorised tenancy deposit schemes<br>("the Tenancy Deposit Scheme") in accordance with the Tenancy Deposit Scheme Rules</div>
<div class="abs field-label" style="top:466px">The INVENTORY</div>
<div class="abs field-box" style="top:466px;left:161px"></div>
<div class="abs caption" style="top:511px;left:165px">means the list of the Landlord's possessions at the Property which has been signed by the Landlord and the Tenant</div>

<!-- signatures -->
<div class="abs party-heading" style="top:567px;left:53px">Landlord</div>
<div class="abs small" style="top:580px;left:53px">Landlord(s)' name(s)</div>
<div class="abs party-heading" style="top:565px;left:274px">Tenant</div>
<div class="abs small" style="top:580px;left:274px">Tenant(s)' name(s)</div>
<div class="abs divider" style="left:261px;top:570px;height:161px"></div>
<div class="abs sign-line" style="left:53px;top:612px;width:197px"></div>
<div class="abs sign-line" style="left:53px;top:639px;width:197px"></div>
<div class="abs sign-line" style="left:53px;top:684px;width:197px"></div>
<div class="abs sign-line" style="left:274px;top:612px;width:196px"></div>
<div class="abs sign-line" style="left:274px;top:639px;width:196px"></div>
<div class="abs sign-line" style="left:274px;top:684px;width:196px"></div>
<div class="abs small" style="top:690px;left:53px">Landlord(s)' signature(s)</div>
<div class="abs small" style="top:690px;left:274px">Tenant(s)' signature(s)</div>

<!-- date -->
<div class="abs small" style="top:690px;left:551px">Date</div>
<div class="abs date-key" style="top:671px;left:576px">D</div>
<div class="abs date-key" style="top:671px;left:591px">D</div>
<div class="abs date-key" style="top:671px;left:632px">M</div>
<div class="abs date-key" style="top:671px;left:647px">M</div>
<div class="abs date-key" style="top:671px;left:688px">Y</div>
<div class="abs date-key" style="top:671px;left:703px">Y</div>
<div class="abs date-key" style="top:671px;left:718px">Y</div>
<div class="abs date-key" style="top:671px;left:733px">Y</div>
<div class="abs date-box" style="top:682px;left:576px"></div>
<div class="abs date-box" style="top:682px;left:591px"></div>
<div class="abs date-box" style="top:682px;left:613px">-</div>
<div class="abs date-box" style="top:682px;left:632px"></div>
<div class="abs date-box" style="top:682px;left:647px"></div>
<div class="abs date-box" style="top:682px;left:669px">-</div>
<div class="abs date-box" style="top:682px;left:688px"></div>
<div class="abs date-box" style="top:682px;left:703px"></div>
<div class="abs date-box" style="top:682px;left:718px"></div>
<div class="abs date-box" style="top:682px;left:733px"></div>

<div class="abs seal-panel"></div>

<!-- witnesses -->
<div class="abs presence" style="top:728px;left:53px">In the presence of:</div>
<div class="abs divider" style="left:261px;top:786px;height:105px"></div>
<div class="abs small" style="top:759px;left:53px">Witness signature</div>
<div class="abs small" style="top:759px;left:274px">Witness signature</div>
<div class="abs sign-line" style="left:53px;top:799px;width:197px"></div>
<div class="abs sign-line" style="left:274px;top:799px;width:196px"></div>
<div class="abs small" style="top:801px;left:53px">Full name</div>
<div class="abs small" style="top:801px;left:274px">Full name</div>
<div class="abs sign-line" style="left:53px;top:829px;width:197px"></div>
<div class="abs sign-line" style="left:274px;top:829px;width:196px"></div>
<div class="abs small" style="top:832px;left:53px">Address</div>
<div class="abs small" style="top:832px;left:274px">Address</div>
<div class="abs sign-line" style="left:53px;top:855px;width:197px"></div>
<div class="abs sign-line" style="left:274px;top:855px;width:196px"></div>
<div class="abs sign-line" style="left:53px;top:881px;width:197px"></div>
<div class="abs sign-line" style="left:274px;top:881px;width:196px"></div>

<!-- notices -->
<div class="abs notice">
  <h3>IMPORTANT NOTICE TO LANDLORDS:</h3>
  <ol>
    <li>The details of 'The LANDLORD' near the top of this Agreement must include an address for the Landlord in England or Wales as well as his/her name, or all names in the case of joint Landlords.</li>
    <li>Always remember to give the written Notice Requiring Possession to the Tenant at least two clear months before the end of the Term if you want the Tenant to vacate.</li>
    <li>Before granting the tenancy agreement, you should check whether your chosen deposit scheme provider requires you to insert any additional terms concerning the deposit into the tenancy agreement or to alter or delete any of the terms appearing in the form below. Details of the websites of the scheme providers are set out in Note 4 for tenants below. Currently only The Rental Deposit Scheme has such requirements.</li>
  </ol>
  <h3>IMPORTANT NOTICE TO TENANTS:</h3>
  <ol>
    <li>In general, if you currently occupy this Property under a protected or statutory tenancy and you give it up to take a new tenancy of the same or other accommodation owned by the same Landlord, that tenancy cannot be an Assured Shorthold Tenancy and this Agreement is not appropriate.</li>
    <li>If you currently occupy this Property under an Assured Tenancy which is not an Assured Shorthold Tenancy your Landlord is not permitted to grant you an Assured Shorthold Tenancy of this Property or of alternative property and this Agreement is not appropriate.</li>
    <li>In England, if the total amount of rent exceeds £100,000 (£25,000 in Wales) per annum, an Assured Shorthold Tenancy cannot be created and this Agreement is not appropriate.</li>
    <li>Further information about the Government-authorised Tenancy Deposit Schemes can be obtained from their websites: The Deposit Guard Service at www.depositguard.example, SafeDeposits at www.safedeposits.example and The Rental Deposit Scheme at www.rentaldisputes.example.</li>
    <li>If your tenancy starts after 1 October 2008, your landlord should provide you with an Energy Performance Certificate.</li>
  </ol>
</div>
<div class="abs footnote">(*delete as appropriate)</div>
</body>
</html>
```